I need a business card design for my new clinic (SPORTS MEDICINE OF KNEE). I am orthopedist, expert in sports surgery, especially knee surgery. I prefer, as colors, the colors of my logo (green, black and white). I already have my logo and should appear on my card. It's good to see my site to have ideas (www.drlucianovarela.com)
It needs contain:
my name: Dr. Luciano Varela
my registration: CRM 584-902
my specialty: Cirurgia do Joelho / Esporte
my address: Centro Executivo - Pinheiral Plaza
Av. Doutor Augusto Brandão Cunha, 2740 sala 0836
Jd. Ipanema - Ribeirão Preto - SP
my phone number: Tel (16) 8245-3908
my clinic phone: (16) 3670-4851
my e-mail: drlucianovarela@mailbox-exemplo.com
my site: www.drlucianovarela.com

Target Market(s)

futures patients

Industry/Entity Type

Clinic

Requirements
Nice to have
• letters not overfilled
straight lines, with few curves

```html
<!DOCTYPE html>
<html lang="pt-BR">
<head>
<meta charset="utf-8">
<title>Cartão de visita – Dr. Luciano Varela</title>
<link rel="stylesheet" href="https://fonts.googleapis.com/css2?family=Arimo:wght@400;700&display=swap">
<style>
  :root {
    --page-bg: #8a8a8a;
    --card-white: #f7f7f5;
    --brand-green: #2aa86a;
    --brand-green-soft: #3fbf80;
    --ink-black: #141414;
    --panel-dark: #1c1c1c;
    --panel-mid: #4a4a4a;
    --text-light: #d6d6d6;
    --text-muted: #b4b4b4;
  }
  * { box-sizing: border-box; margin: 0; padding: 0; }
  html, body {
    width: 1200px; height: 1200px; overflow: hidden;
    background: var(--page-bg);
    font-family: "Arimo", Arial, sans-serif;
  }
  .stage {
    width: 1200px; height: 1200px;
    display: flex; align-items: center; justify-content: center;
  }
  .business-card {
    width: 1000px; height: 560px;
    background: var(--card-white);
    display: flex; flex-direction: column;
    box-shadow: 0 20px 50px rgba(0,0,0,.35);
  }
  .card-top {
    height: 222px;
    display: flex; align-items: center;
    padding-left: 64px;
  }
  .brand {
    display: flex; align-items: center; gap: 20px;
  }
  .brand-square {
    width: 64px; height: 64px;
    background: var(--ink-black);
  }
  .brand-name {
    font-size: 64px; font-weight: 700;
    color: var(--ink-black);
    letter-spacing: 2px;
  }
  .green-band {
    height: 10px; background: var(--brand-green);
  }
  .card-bottom {
    flex: 1;
    background: radial-gradient(ellipse at 62% 45%, var(--panel-mid) 0%, var(--panel-dark) 70%);
    display: flex;
    padding: 30px 0 0 64px;
  }
  .contact-list {
    width: 560px;
    list-style: none;
    font-size: 18px; line-height: 1.5;
    color: var(--text-light);
  }
  .contact-label { color: var(--brand-green-soft); }
  .divider {
    width: 2px; height: 200px;
    background: var(--brand-green);
    margin-top: -30px;
  }
  .doctor {
    padding-left: 26px; padding-top: 4px;
  }
  .doctor-name {
    font-size: 28px; font-weight: 700;
    color: var(--brand-green-soft);
    margin-bottom: 8px;
  }
  .doctor-detail {
    font-size: 19px; line-height: 1.4;
    color: var(--text-muted);
  }
</style>
</head>
<body>
<main class="stage">
  <article class="business-card">
    <header class="card-top">
      <div class="brand">
        <span class="brand-square"></span>
        <span class="brand-name">VARELA</span>
      </div>
    </header>
    <div class="green-band"></div>
    <section class="card-bottom">
      <ul class="contact-list">
        <li><span class="contact-label">A:</span> Centro Executivo - Pinheiral Plaza</li>
        <li>Av. Doutor Augusto Brandão Cunha,</li>
        <li>2740 sala 0836</li>
        <li>Jd. Ipanema - Ribeirão Preto - SP</li>
        <li><span class="contact-label">T (pessoal):</span> (16) 8245-3908</li>
        <li><span class="contact-label">T (clínica):</span> (16) 3670-4851</li>
        <li><span class="contact-label">E:</span> drlucianovarela@mailbox-exemplo.com</li>
        <li><span class="contact-label">W:</span> www.drlucianovarela.com</li>
      </ul>
      <div class="divider"></div>
      <div class="doctor">
        <p class="doctor-name">Dr. Luciano Varela</p>
        <p class="doctor-detail">Cirurgia do Joelho / Esporte</p>
        <p class="doctor-detail">CRM 584-902</p>
      </div>
    </section>
  </article>
</main>
</body>
</html>
```